Redesign my business cards

I would like pretty much all the same information as my current business cards but redesigned to stand out more and be more unique photo uploaded to show my current business cards don’t mind if you want to remove or replace I for on the back

```html
<!DOCTYPE html>
<html lang="en">
<head>
<meta charset="utf-8">
<title>Detailing Price List</title>
<link rel="stylesheet" href="https://fonts.googleapis.com/css2?family=Montserrat:wght@300;800&family=Exo+2:ital,wght@1,800&display=swap">
<style>
  :root {
    --navy: #133d7a;
    --navy-deep: #0d2d5e;
    --white: #ffffff;
    --body-text: #e4eaf4;
    --rule: rgba(255, 255, 255, 0.16);
    --price-red: #f4525a;
    --band-blue-top: #1f5cb6;
    --band-blue-mid: #5475ff;
    --band-blue-bottom: #2c7de0;
    --band-light-top: #3fb4ff;
    --band-light-bottom: #f4faff;
  }
  * { margin: 0; padding: 0; box-sizing: border-box; }
  html, body { width: 1200px; height: 686px; overflow: hidden; background: var(--navy); }
  .card {
    position: relative;
    width: 1200px;
    height: 686px;
    overflow: hidden;
    background: linear-gradient(100deg, var(--navy) 0%, var(--navy) 55%, var(--navy-deep) 100%);
    font-family: "Montserrat", Arial, sans-serif;
  }
  .bands { position: absolute; inset: 0; width: 1200px; height: 686px; }
  .side-rail {
    position: absolute;
    left: 0; top: 0;
    width: 10px; height: 686px;
    background: var(--price-red);
  }
  .service {
    position: absolute;
    left: 48px;
    width: 800px;
  }
  .service-title {
    font-weight: 800;
    font-size: 44px;
    line-height: 48px;
    color: var(--white);
    letter-spacing: 0.3px;
    white-space: nowrap;
  }
  .service-features {
    margin-top: 4px;
    font-weight: 300;
    font-size: 22px;
    line-height: 28px;
    color: var(--body-text);
  }
  .line { display: block; white-space: nowrap; }
  .interior { top: 44px; }
  .exterior { top: 244px; }
  .full { top: 412px; }
  .divider {
    position: absolute;
    left: 48px;
    width: 800px;
    height: 1px;
    background: var(--rule);
  }
  .divider-one { top: 222px; }
  .divider-two { top: 390px; }
  .price {
    position: absolute;
    right: 360px;
    font-family: "Exo 2", Arial, sans-serif;
    font-style: italic;
    font-weight: 800;
    font-size: 58px;
    line-height: 58px;
    color: var(--white);
    text-shadow: 2px 2px 3px rgba(0, 0, 0, 0.35);
    letter-spacing: -1px;
    text-align: right;
  }
  .price .currency { color: var(--price-red); }
  .price::after {
    content: "";
    display: block;
    width: 54px;
    height: 4px;
    margin: 8px 0 0 auto;
    background: var(--price-red);
    transform: skewX(-20deg);
  }
  .price-interior { top: 40px; }
  .price-exterior { top: 240px; }
  .price-full { top: 408px; }
</style>
</head>
<body>
<main class="card">
  <svg class="bands" viewBox="0 0 1200 686" aria-hidden="true">
    <defs>
      <linearGradient id="bandBlue" x1="0" y1="0" x2="0" y2="1">
        <stop offset="0" stop-color="var(--band-blue-top)"/>
        <stop offset="0.45" stop-color="var(--band-blue-mid)"/>
        <stop offset="1" stop-color="var(--band-blue-bottom)"/>
      </linearGradient>
      <linearGradient id="bandLight" x1="0" y1="0" x2="0" y2="1">
        <stop offset="0" stop-color="var(--band-light-top)"/>
        <stop offset="1" stop-color="var(--band-light-bottom)"/>
      </linearGradient>
    </defs>
    <polygon points="975,0 1030,0 935,686 880,686" fill="url(#bandLight)"/>
    <polygon points="1043,0 1051,0 956,686 948,686" fill="var(--price-red)"/>
    <polygon points="1064,0 1200,0 1200,686 969,686" fill="url(#bandBlue)"/>
  </svg>
  <div class="side-rail" aria-hidden="true"></div>

  <section class="service interior">
    <h2 class="service-title">INTERIOR DETAIL</h2>
    <p class="service-features">
      <span class="line">vacuum &amp; deep clean of carpets &amp; upholstery</span>
      <span class="line">or leather treatment · interior trim clean &amp;</span>
      <span class="line">condition · window polish and treatment ·</span>
      <span class="line">steam clean and stain removal</span>
    </p>
  </section>
  <div class="price price-interior"><span class="currency">$</span>150</div>

  <div class="divider divider-one" aria-hidden="true"></div>

  <section class="service exterior">
    <h2 class="service-title">EXTERIOR DETAIL</h2>
    <p class="service-features">
      <span class="line">extreme wash &amp; polish · exterior trim reviver</span>
      <span class="line">&amp; protector · window polish &amp; treatment ·</span>
      <span class="line">tyre dressing · engine bay cleaning</span>
    </p>
  </section>
  <div class="price price-exterior"><span class="currency">$</span>250</div>

  <div class="divider divider-two" aria-hidden="true"></div>

  <section class="service full">
    <h2 class="service-title">FULL EXTREME DETAIL</h2>
    <p class="service-features">
      <span class="line">extreme wash &amp; polish · tyre dressing ·</span>
      <span class="line">engine bay cleaned · vacuum &amp; deep clean of</span>
      <span class="line">carpets &amp; upholstery or leather treatment ·</span>
      <span class="line">interior &amp; exterior trim reviver &amp; protector ·</span>
      <span class="line">window polish and treatment</span>
    </p>
  </section>
  <div class="price price-full"><span class="currency">$</span>350</div>
</main>
</body>
</html>
```